Harbourline Blinds & Shutters

It Needs to look classy as my target is the upper end of the blind market
I need a Logo design on front and description on back of what i do:
- Roller Blinds
- Vertical Blinds
- Venetian Blinds
- Plantation Shutters
- Aluminum External Shutters
and contact details
Gavin
0418527306
and
Terry
0421690358
Updates
Hi Guys,
Sorry for the no feedback but i was waiting on my logo design. But its done now i have uploaded it. so if you could take a look and send through some designs
Reason: my logo was just finished an i just uploaded it today really dont understand why my deadline has been rached foe my bizcards as it states no deadline. But please extend
Target Market(s)
People that live on the coast and are looking for classy good quality blinds and shutters
Font styles to use
Other font styles liked:
- Copperplate Gothic,open to suggestion
Look and feel
Each slider illustrates characteristics of the customer's brand and the style your logo design should communicate.

```html
<!DOCTYPE html>
<html lang="en">
<head>
<meta charset="utf-8">
<title>Harbourline Blinds &amp; Shutters – Business Card</title>
<link rel="stylesheet" href="https://fonts.googleapis.com/css2?family=Arimo:wght@400;700&display=swap">
<style>
  :root {
    --backdrop: #cfe9e0;
    --card-red: #ff0000;
    --card-black: #000000;
    --ink-white: #ffffff;
    --ghost: #1b1b1b;
    --card-radius: 34px;
  }
  * { box-sizing: border-box; margin: 0; padding: 0; }
  html, body {
    width: 1200px; height: 856px; overflow: hidden;
    background: var(--backdrop);
    font-family: "Arimo", Arial, sans-serif;
  }
  .canvas { position: relative; width: 1200px; height: 856px; }

  .card {
    position: absolute; width: 525px; height: 300px;
    border-radius: var(--card-radius); overflow: hidden;
  }

  /* Front */
  .card--front { left: 110px; top: 440px; background: var(--card-red); }
  .brand-name {
    position: absolute; left: 44px; top: 112px; width: 230px;
    color: var(--card-black); font-weight: 700; line-height: 1;
  }
  .brand-name__main { display: block; font-size: 40px; letter-spacing: 0; }
  .brand-name__sub { display: block; font-size: 15px; letter-spacing: 1.2px; margin-top: 10px; }

  .contacts {
    position: absolute; left: 300px; top: 128px;
    color: var(--ink-white); font-size: 15px; line-height: 1.4;
  }
  .contact { display: flex; gap: 6px; align-items: baseline; }
  .contact__name { font-weight: 700; font-size: 17px; letter-spacing: 0.5px; width: 64px; }
  .contact__phone { letter-spacing: 0.6px; }

  /* Back */
  .card--back { left: 585px; top: 90px; background: var(--card-black); }
  .ghost-name {
    position: absolute; left: 40px; top: 46px; width: 445px;
    color: var(--ghost); font-weight: 700; line-height: 1; text-align: right;
  }
  .ghost-name__main { display: block; font-size: 76px; letter-spacing: -1px; white-space: nowrap; }
  .ghost-name__sub { display: block; font-size: 28px; letter-spacing: 2px; margin-top: 14px; white-space: nowrap; }
  .services {
    position: absolute; left: 0; right: 0; top: 170px;
    list-style: none; color: var(--ink-white); font-size: 14px; letter-spacing: 0.4px;
    line-height: 1.35;
  }
  .services__row { display: flex; justify-content: center; align-items: center; gap: 6px; }
  .services__divider {
    display: inline-block; width: 3px; height: 12px; background: var(--card-red);
  }
</style>
</head>
<body>
<main class="canvas">

  <section class="card card--back" aria-label="Business card back">
    <div class="ghost-name" aria-hidden="true">
      <span class="ghost-name__main">Harbourline</span>
      <span class="ghost-name__sub">BLINDS &amp; SHUTTERS</span>
    </div>
    <ul class="services">
      <li class="services__row">
        <span>Roller Blinds</span><span class="services__divider"></span>
        <span>Vertical Blinds</span><span class="services__divider"></span>
        <span>Venetian Blinds</span>
      </li>
      <li class="services__row">
        <span>Plantation Shutters</span><span class="services__divider"></span>
        <span>Aluminum External Shutters</span>
      </li>
    </ul>
  </section>

  <section class="card card--front" aria-label="Business card front">
    <h1 class="brand-name">
      <span class="brand-name__main">Harbourline</span>
      <span class="brand-name__sub">BLINDS &amp; SHUTTERS</span>
    </h1>
    <div class="contacts">
      <p class="contact"><span class="contact__name">GAVIN</span><span class="contact__phone">- 0418527306</span></p>
      <p class="contact"><span class="contact__name">TERRY</span><span class="contact__phone">- 0421690358</span></p>
    </div>
  </section>

</main>
</body>
</html>
```